Private School Website Revamp

We need a new design for the private school's website revamp. The new website will be using WordPress CMS, but we will be using it to handle custom data types, not blogs - so the content will not be typical blog-style.

The school has indicated the following template which they like, and our design to follow the design style.
http://qrv7.layoutkiosk-demo.com/sitekit_48215/
However, follow the school's colour-theme and sitemap.

Colour-theme: White, Green (refer to current website - www.morvelan.com.sg)

Sitemap: (for navigation menu)
- Home
- Academic & Examination Board
- Our Philosophy
- Our Programmes
+ Preparatory Courses
+ Tuition Classes
+ Study Tours
- Our Hostel
- Trial Tests
+ English
+ Mathematics
- Contact Us

Target Market(s)

Parents looking for private school services.
Existing students of the private school accessing trial tests.

Industry/Entity Type

School

Requirements
Must have
• Homepage design to include
• - Logo, navigation menu, search box
• - Featured area/slideshow (see prefered template above)
• - Section for Preparatory Courses
• - Section for Tuition Classes
• - Section for Study Tours
• - Section for Hostel Stay
• - Awards & Certification box
• - Footer contact details
Nice to have
• - Pictures of happy students
• - The Message from Director box is "nice to have", but no necessary if it does not fit into homepage design.

```html
<!DOCTYPE html>
<html lang="en">
<head>
<meta charset="utf-8">
<title>Morvelan Private School</title>
<link rel="stylesheet" href="https://fonts.googleapis.com/css2?family=Arimo:wght@400;700&display=swap">
<style>
:root{
  --sky-top:#9fdcf6;
  --sky-bottom:#ffffff;
  --green:#5aa82a;
  --green-light:#a6dc74;
  --green-dark:#2f6d12;
  --logo-dark:#0f3d12;
  --text:#444444;
  --text-dark:#222222;
  --border:#dcdcdc;
  --panel:#ffffff;
  --badge-blue:#0d4c93;
  --badge-green:#6c8d63;
}
*{box-sizing:border-box;margin:0;padding:0}
html,body{width:985px;height:1200px;overflow:hidden}
body{
  position:relative;
  font-family:"Arimo",Arial,sans-serif;
  color:var(--text);
  background:linear-gradient(to bottom,var(--sky-top) 0,#dff3fc 420px,var(--sky-bottom) 700px);
}
.abs{position:absolute}
.brand{left:111px;top:56px;display:flex;align-items:center;gap:8px;color:var(--logo-dark);font-weight:700;font-size:20px;letter-spacing:.5px}
.brand-mark{width:18px;height:18px;background:var(--logo-dark)}
.search{left:715px;top:30px;width:152px;height:21px;display:flex}
.search-field{flex:1;background:#fff;border:1px solid #c9d3d8}
.search-btn{width:24px;border:1px solid #b8c2c7;background:linear-gradient(#fafafa,#dcdcdc);display:flex;align-items:center;justify-content:center}
.nav{left:349px;top:82px;display:flex;align-items:center;font-size:10.5px;font-weight:700;color:var(--text-dark)}
.nav a{color:inherit;text-decoration:none}
.nav .sep{margin:0 5px;font-weight:400}
.nav .current{background:var(--green-dark);color:#fff;border-radius:4px;padding:5px 6px;margin-right:6px}
.panel{background:var(--panel);border:1px solid var(--border);border-radius:8px}
.hero{left:111px;top:120px;width:756px;height:219px;overflow:hidden}
.hero .photo{width:100%;height:100%;background:linear-gradient(90deg,#e6e6e6,#cfc6bc 30%,#b7a596 55%,#d2cbc4 80%,#e8e8e8)}
.card{width:242px;height:166px;top:352px}
.card-head{position:absolute;left:8px;top:8px;width:224px;height:50px;border-radius:6px;background:linear-gradient(var(--green),var(--green-light));color:#fff;font-weight:700;font-size:12.5px;display:flex;align-items:center;padding-left:72px;letter-spacing:.2px}
.card-icon{position:absolute;left:10px;top:4px;width:50px;height:46px;border-radius:8px}
.card-rule{position:absolute;left:8px;right:8px;top:68px;border-top:1px solid #e4e4e4}
.card-body{position:absolute;left:10px;right:12px;top:80px;font-size:9.2px;line-height:11px}
.card-body strong{display:block;font-size:11px;line-height:13px;color:var(--text-dark);margin-bottom:4px}
.more{position:absolute;display:flex;align-items:center;gap:4px;font-size:10px;color:var(--text-dark)}
.section-head{position:absolute;left:8px;top:9px;height:33px;border-radius:6px;background:linear-gradient(var(--green),var(--green-light));color:#fff;font-weight:700;font-size:12.5px;display:flex;align-items:center;padding-left:15px}
.director{left:111px;top:527px;width:499px;height:292px}
.director-text{position:absolute;left:9px;right:10px;top:48px;font-size:9.2px;line-height:10.6px}
.portrait{float:left;width:76px;height:72px;margin:3px 8px 4px 0;border-radius:5px;background:linear-gradient(#b9b0a4,#6e6760)}
.hostel{left:626px;top:527px;width:241px;height:292px}
.hostel-item{position:absolute;left:8px;width:224px}
.hostel-photo{position:absolute;left:0;top:0;width:76px;height:72px;border-radius:4px}
.hostel-title{position:absolute;left:82px;top:0;font-size:13px;color:var(--text-dark)}
.hostel-body{position:absolute;left:84px;top:18px;width:142px;font-size:9.2px;line-height:10.7px}
.hostel-rule{position:absolute;left:8px;right:8px;top:163px;border-top:1px solid #e4e4e4}
.strip{left:111px;top:828px;width:498px;height:127px;border-radius:8px;background:linear-gradient(90deg,#d9a68a,#c34a3b 30%,#e7d9bf 50%,#8fb6d5 72%,#6aa448)}
.awards{left:626px;top:828px;width:241px;height:128px}
.badge{position:absolute;top:52px;height:64px;border-radius:3px}
.footer{left:111px;top:972px;width:756px;height:175px;border-radius:8px;background:linear-gradient(var(--green),#5d9b33);color:#fff;font-size:9.5px;line-height:11px}
.footer h2{position:absolute;left:24px;top:29px;font-size:10.5px;color:#234f10;font-weight:700}
.footer address{position:absolute;left:24px;top:52px;font-style:normal}
.footer .brand-foot{position:absolute;left:592px;top:72px;display:flex;align-items:center;gap:6px;color:var(--logo-dark);font-weight:700;font-size:14px}
.footer .brand-foot span{width:13px;height:13px;background:var(--logo-dark)}
.copyright{left:0;width:985px;top:1158px;text-align:center;font-size:8.5px;color:var(--text-dark)}
</style>
</head>
<body>

<div class="abs brand"><span class="brand-mark"></span>MORVELAN PRIVATE SCHOOL</div>

<form class="abs search">
  <div class="search-field"></div>
  <div class="search-btn">
    <svg width="12" height="12" viewBox="0 0 12 12"><circle cx="5" cy="5" r="3.6" fill="none" stroke="#555" stroke-width="1.4"/><line x1="7.6" y1="7.6" x2="11" y2="11" stroke="#555" stroke-width="1.8"/></svg>
  </div>
</form>

<nav class="abs nav">
  <a class="current" href="#">Home</a>
  <a href="#">Academic &amp; Examination Board</a><span class="sep">|</span>
  <a href="#">Our Philosophy</a><span class="sep">|</span>
  <a href="#">Our Programmes</a><span class="sep">|</span>
  <a href="#">Our Hostel</a><span class="sep">|</span>
  <a href="#">Trial Tests</a><span class="sep">|</span>
  <a href="#">Contact Us</a>
</nav>

<section class="abs panel hero">
  <div class="photo" role="img" aria-label="Group photo of smiling students"></div>
</section>

<section class="abs panel card" style="left:111px">
  <div class="card-head"><div class="card-icon" role="img" aria-label="Books icon" style="background:linear-gradient(#7fc0f0,#2c6fbf)"></div>PREPARATORY COURSES</div>
  <div class="card-rule"></div>
  <p class="card-body">Our Preparatory Course is designed for international students who intend to enrol in a local government school.</p>
  <a class="more" style="left:156px;top:137px"><svg width="16" height="16" viewBox="0 0 16 16"><circle cx="8" cy="8" r="8" fill="#5aa82a"/><path d="M5 5l3 3-3 3M8.5 5l3 3-3 3" fill="none" stroke="#fff" stroke-width="1.4"/></svg>Read more...</a>
</section>

<section class="abs panel card" style="left:368px">
  <div class="card-head"><div class="card-icon" role="img" aria-label="Pencil icon" style="background:linear-gradient(#f4c27a,#d9622a)"></div>TUITION CLASSES</div>
  <div class="card-rule"></div>
  <p class="card-body">Morvelan Private School is registered with the Ministry of Education since 2002 and is managed by a group of professionals, who were formerly senior officers of the Ministry of Education.</p>
  <a class="more" style="left:157px;top:137px"><svg width="16" height="16" viewBox="0 0 16 16"><circle cx="8" cy="8" r="8" fill="#5aa82a"/><path d="M5 5l3 3-3 3M8.5 5l3 3-3 3" fill="none" stroke="#fff" stroke-width="1.4"/></svg>Read more...</a>
</section>

<section class="abs panel card" style="left:626px;width:241px">
  <div class="card-head"><div class="card-icon" role="img" aria-label="Globe in hands icon" style="background:linear-gradient(#6fb7f2,#f0a343)"></div>STUDY TOURS</div>
  <div class="card-rule"></div>
  <div class="card-body" style="top:78px"><strong>The holidays are coming!<br>Join our study tours!</strong>We offer quality immersion programme to foreign participants coming to Singapore.</div>
  <a class="more" style="left:157px;top:137px"><svg width="16" height="16" viewBox="0 0 16 16"><circle cx="8" cy="8" r="8" fill="#5aa82a"/><path d="M5 5l3 3-3 3M8.5 5l3 3-3 3" fill="none" stroke="#fff" stroke-width="1.4"/></svg>Read more...</a>
</section>

<section class="abs panel director">
  <h2 class="section-head" style="width:480px">DIRECTOR MESSAGE</h2>
  <div class="director-text">
    <p style="margin-bottom:4px">Morvelan Private School was founded to meet the growing demand of foreign students seeking an effective bilingual education in Singapore.</p>
    <div class="portrait" role="img" aria-label="Portrait of the school director"></div>
    <p style="margin-bottom:11px">We are managed by a group of professionals who are formerly Ministry of Education senior officers and we have a team of dedicated, qualified and experienced part time teachers who are committed to help you succeed.</p>
    <p>In order for our students to focus their full attention on their studies, we provide a conducive learning environment through a low teacher-student ratio of 1:15 and properly equipped classrooms. There are 5 such classrooms in the school, able to hold between 11 to 15 students per class, based on the guidelines prescribed by the Ministry of Education. With this, we wish you every success in your learning journey with us and we believe you will find your journey here an excellent chance for personal growth and development.</p>
    <p style="margin-top:23px">Yours sincerely,</p>
    <p style="margin-top:14px"><b style="color:var(--text-dark)">Mr Lim Wei Hao</b><br>Director<br>Morvelan Private School</p>
  </div>
</section>

<section class="abs panel hostel">
  <h2 class="section-head" style="width:223px">HOSTEL STAY</h2>
  <div class="hostel-item" style="top:50px">
    <div class="hostel-photo" role="img" aria-label="Boys hostel apartment block" style="background:linear-gradient(#c9b9a6,#a77a5a 60%,#7d9a6a)"></div>
    <h3 class="hostel-title" style="font-weight:400">Boys</h3>
    <p class="hostel-body">The Boys Hostel is a 3-storey apartment block located next to the Church of Bellmont near the junction of Harlow Parade Road and Tessmer Road.</p>
  </div>
  <a class="more" style="left:8px;top:131px"><svg width="16" height="16" viewBox="0 0 16 16"><circle cx="8" cy="8" r="8" fill="#5aa82a"/><path d="M5 5l3 3-3 3M8.5 5l3 3-3 3" fill="none" stroke="#fff" stroke-width="1.4"/></svg>Read more...</a>
  <div class="hostel-rule"></div>
  <div class="hostel-item" style="top:179px">
    <div class="hostel-photo" role="img" aria-label="Girls hostel house" style="background:linear-gradient(#dcdad6,#8a5b48 55%,#6f8c57)"></div>
    <h3 class="hostel-title" style="font-weight:400">Girls</h3>
    <p class="hostel-body">The Girls Hostel comprises 6 deluxe properties located in the quiet residential neighborhood in Fernvale Heights. located near many schools.</p>
  </div>
  <a class="more" style="left:8px;top:259px"><svg width="16" height="16" viewBox="0 0 16 16"><circle cx="8" cy="8" r="8" fill="#5aa82a"/><path d="M5 5l3 3-3 3M8.5 5l3 3-3 3" fill="none" stroke="#fff" stroke-width="1.4"/></svg>Read more...</a>
</section>

<div class="abs strip" role="img" aria-label="Photos of students studying and children in class"></div>

<section class="abs panel awards">
  <h2 class="section-head" style="width:223px">AWARDS &amp; CERTIFICATION</h2>
  <div class="badge" style="left:9px;width:121px;background:var(--badge-blue)"></div>
  <div class="badge" style="left:138px;width:92px;background:var(--badge-green)"></div>
</section>

<footer class="abs footer">
  <h2>CONTACT US</h2>
  <address>18 Keller Ridge Ave 41<br>Ashwood Community Hub, #03-02<br>S(604417)<br><br>Tel: +65 6418 2275<br>Fax: +65 6418 2290<br>Email: school@morvelan.com.sg</address>
  <div class="brand-foot"><span></span>MORVELAN</div>
</footer>

<p class="abs copyright">© 2008. Morvelan Private School. All rights reserved</p>

</body>
</html>
```